Business card for STEADYWAVE

Please design professional business card for IT consulting firm STEADYWAVE INC.
Use logo attached.
Use information from sample qNode business card attached.
replace qnode inc with STEADYWAVE INC.
as well as qnodeinc.com with steadywave.example

```html
<!DOCTYPE html>
<html lang="en">
<head>
<meta charset="utf-8">
<title>Steadywave Business Card</title>
<link rel="stylesheet" href="https://fonts.googleapis.com/css2?family=Jost:wght@300;400;500&display=swap">
<style>
  :root {
    --page: #cfcfd1;
    --card-white: #f7f7f7;
    --card-black: #1e1e1e;
    --ink: #111111;
    --paper-text: #ffffff;
    --accent: #f08a1c;
  }
  * { margin: 0; padding: 0; box-sizing: border-box; }
  html, body {
    width: 1200px; height: 800px; overflow: hidden;
    background: var(--page);
    font-family: "Jost", sans-serif;
  }
  .sheet {
    width: 1200px; height: 800px;
    display: flex; align-items: center; justify-content: center; gap: 40px;
  }
  .card {
    position: relative;
    width: 540px; height: 310px;
    border-radius: 22px;
    overflow: hidden;
    box-shadow: 0 10px 24px rgba(0,0,0,0.18);
  }
  /* Front */
  .card--front { background: var(--card-white); }
  .front__band {
    position: absolute; left: 0; top: 178px;
    width: 100%; height: 108px;
    background: var(--card-black);
  }
  .front__column {
    position: absolute; left: 400px; top: 0;
    width: 140px; height: 286px;
    background: var(--card-black);
  }
  .wordmark {
    font-weight: 500; letter-spacing: 0; line-height: 1;
  }
  .front__brand {
    position: absolute; left: 34px; top: 44px;
    color: var(--ink); font-size: 44px;
  }
  .front__person { position: absolute; left: 36px; top: 108px; }
  .person__name {
    font-weight: 500; font-size: 20px; color: var(--ink); letter-spacing: 0.02em;
  }
  .person__title {
    font-weight: 400; font-size: 14px; color: var(--accent);
    letter-spacing: 0.04em; margin-top: 2px;
  }
  .front__contact {
    position: absolute; left: 36px; top: 190px;
    color: var(--paper-text); font-weight: 300; font-size: 12.5px; line-height: 16px;
    font-style: normal;
  }
  .contact__company { font-weight: 500; }
  .contact__row { display: flex; align-items: center; gap: 6px; }
  .contact__row svg { width: 11px; height: 11px; flex: none; }
  .contact__gap { margin-left: 10px; }
  /* Back */
  .card--back {
    background: var(--card-black);
    display: flex; align-items: center; justify-content: center;
  }
  .back__brand { color: var(--paper-text); font-size: 46px; }
</style>
</head>
<body>
<main class="sheet">
  <section class="card card--front" aria-label="Card front">
    <div class="front__band"></div>
    <div class="front__column"></div>
    <div class="front__brand wordmark">Steadywave</div>
    <div class="front__person">
      <p class="person__name">DANIEL VORONOV, P.ENG.</p>
      <p class="person__title">GENERAL MANAGER</p>
    </div>
    <address class="front__contact">
      <p class="contact__company">STEADYWAVE INC</p>
      <p>1820 Harbour Ln., Suite 204</p>
      <p>Lakeview, Ontario, A1B 2C3, Canada</p>
      <p class="contact__row">
        <svg viewBox="0 0 12 12" aria-hidden="true"><path d="M2 1h2.5l1 3-1.5 1a6 6 0 0 0 3 3l1-1.5 3 1V10a1 1 0 0 1-1 1A9 9 0 0 1 1 2a1 1 0 0 1 1-1z" fill="var(--accent)"/></svg>
        (555) 014-2200 ext.201
        <svg class="contact__gap" viewBox="0 0 12 12" aria-hidden="true"><rect x="3" y="0.8" width="6" height="10.4" rx="1" fill="none" stroke="var(--accent)" stroke-width="1.4"/></svg>
        (555) 019-3344
      </p>
      <p class="contact__row">
        <svg viewBox="0 0 12 12" aria-hidden="true"><rect x="0.8" y="2.5" width="10.4" height="7" fill="var(--accent)"/><path d="M1 3l5 4 5-4" fill="none" stroke="var(--card-black)" stroke-width="1"/></svg>
        dvoronov@steadywave.example
        <svg class="contact__gap" viewBox="0 0 12 12" aria-hidden="true"><circle cx="6" cy="6" r="5" fill="none" stroke="var(--accent)" stroke-width="1.4"/><path d="M1 6h10M6 1c-2.5 3-2.5 7 0 10M6 1c2.5 3 2.5 7 0 10" fill="none" stroke="var(--accent)" stroke-width="1"/></svg>
        www.steadywave.example
      </p>
    </address>
  </section>

  <section class="card card--back" aria-label="Card back">
    <div class="back__brand wordmark">Steadywave</div>
  </section>
</main>
</body>
</html>
```